Envelope Design - Winner can do follow-up business

- Marvuno.com is a Swiss-based online store selling business shirts and accessories for business men
- Please visit the webpage to make yourself familiar with the company. Although the text is in German, with Google translator you should be able to understand the main content.
- Our clients are mainly business men between 30 and 60 years old. Mostly with a high income working in the service industry (banking, insurance, lawyers, etc.). Sometimes there wives purchase the shirts for them ;-)
- The colors and the logo are given, as they are also used for the print materials (please see files in attachment)
- I am running several businesses and often need a talented web designer --> the winner gets substantial follow-up business
your task:
-for our company we need a new envelope design
-It should be simple and modern
-please use one of the logos in the followings.
-suprise me :)

```html
<!DOCTYPE html>
<html lang="en">
<head>
<meta charset="utf-8">
<title>Marvuno Envelope</title>
<link rel="stylesheet" href="https://fonts.googleapis.com/css2?family=Montserrat:wght@500;600&family=Open+Sans:wght@400&display=swap">
<style>
  :root {
    --backdrop: #ecebe8;
    --paper: #ffffff;
    --envelope-inside: #e6e6e8;
    --edge: #a9a9a9;
    --flap-coral: #ec8868;
    --flap-butter: #f6e3a0;
    --flap-salmon: #f9ad93;
    --flap-cream: #fff0bf;
    --tile-cream: #fff4d2;
    --tile-peach: #fde4c0;
    --brand-gold: #e2cf5c;
    --ink: #1d1d1d;
    --accent-red: #e8392b;
  }
  * { margin: 0; padding: 0; box-sizing: border-box; }
  html, body { width: 1200px; height: 1082px; overflow: hidden; }
  body {
    background: var(--backdrop);
    font-family: "Open Sans", Arial, sans-serif;
    position: relative;
  }
  .envelope {
    position: absolute;
    width: 1010px;
    height: 475px;
    border: 1px solid var(--edge);
    overflow: hidden;
  }
  .flap {
    position: absolute;
    left: 0;
    top: 0;
    width: 100%;
    height: 170px;
  }
  .flap-name {
    position: absolute;
    left: 0;
    width: 100%;
    text-align: center;
    font-family: "Montserrat", Arial, sans-serif;
    font-weight: 600;
    color: var(--ink);
  }
  .envelope-back {
    left: 133px;
    top: 95px;
    background: var(--envelope-inside);
  }
  .envelope-back .flap-name {
    top: 58px;
    font-size: 34px;
    letter-spacing: 4px;
  }
  .envelope-open {
    left: 51px;
    top: 287px;
    background: var(--paper);
  }
  .envelope-open .flap-name {
    top: 76px;
    font-size: 30px;
    letter-spacing: 3px;
  }
  .envelope-front {
    left: 73px;
    top: 563px;
    width: 1011px;
    height: 476px;
    background: var(--paper);
  }
  .front-pattern {
    position: absolute;
    inset: 0;
    width: 100%;
    height: 100%;
  }
  .brand-name {
    position: absolute;
    left: 187px;
    top: 232px;
    font-family: "Montserrat", Arial, sans-serif;
    font-weight: 500;
    font-size: 44px;
    letter-spacing: 4px;
    color: var(--brand-gold);
  }
  .web-address {
    position: absolute;
    left: 0;
    top: 364px;
    width: 144px;
    text-align: center;
    font-size: 19px;
    line-height: 24px;
    color: var(--ink);
  }
  .web-address svg { display: block; margin: 0 auto 2px; }
  .street-address {
    position: absolute;
    right: 28px;
    bottom: 22px;
    display: flex;
    align-items: center;
    gap: 12px;
    font-size: 19px;
    color: var(--ink);
  }
</style>
</head>
<body>

<section class="envelope envelope-back">
  <svg class="flap" viewBox="0 0 1010 170" preserveAspectRatio="none" role="img" aria-label="Envelope flap with coral and butter diamond pattern">
    <defs>
      <linearGradient id="backFlapTone" x1="0" y1="0" x2="1" y2="0">
        <stop offset="0" stop-color="var(--flap-coral)"/>
        <stop offset="0.5" stop-color="var(--flap-butter)"/>
        <stop offset="1" stop-color="var(--flap-coral)"/>
      </linearGradient>
    </defs>
    <path d="M0 0 H1010 C998 40 985 58 940 68 L545 152 C520 159 490 159 465 152 L70 68 C25 58 12 40 0 0 Z" fill="url(#backFlapTone)"/>
  </svg>
  <div class="flap-name">MARVUNO</div>
</section>

<section class="envelope envelope-open">
  <svg class="flap" viewBox="0 0 1010 170" preserveAspectRatio="none" role="img" aria-label="Envelope flap with salmon and cream diamond pattern">
    <defs>
      <linearGradient id="openFlapTone" x1="0" y1="0" x2="1" y2="0">
        <stop offset="0" stop-color="var(--flap-cream)"/>
        <stop offset="0.5" stop-color="var(--flap-salmon)"/>
        <stop offset="1" stop-color="var(--flap-cream)"/>
      </linearGradient>
    </defs>
    <path d="M0 0 H1010 C998 40 985 68 940 78 L545 152 C520 159 490 159 465 152 L70 78 C25 68 12 40 0 0 Z" fill="url(#openFlapTone)"/>
  </svg>
  <div class="flap-name">MARVUNO</div>
</section>

<section class="envelope envelope-front">
  <svg class="front-pattern" viewBox="0 0 1011 476" preserveAspectRatio="none" role="img" aria-label="Soft cream and peach diamond pattern on the left side">
    <defs>
      <linearGradient id="tileTone" x1="0" y1="0" x2="1" y2="1">
        <stop offset="0" stop-color="var(--tile-cream)"/>
        <stop offset="1" stop-color="var(--tile-peach)"/>
      </linearGradient>
    </defs>
    <polygon points="0,0 386,0 140,246 363,476 0,476" fill="url(#tileTone)"/>
  </svg>

  <div class="brand-name">MARVUNO</div>

  <div class="web-address">
    <svg width="22" height="22" viewBox="0 0 22 22" aria-hidden="true">
      <g fill="none" stroke="var(--accent-red)" stroke-width="1.5">
        <circle cx="11" cy="11" r="9.5"/>
        <ellipse cx="11" cy="11" rx="4.5" ry="9.5"/>
        <line x1="1.5" y1="11" x2="20.5" y2="11"/>
        <line x1="3" y1="6" x2="19" y2="6"/>
        <line x1="3" y1="16" x2="19" y2="16"/>
      </g>
    </svg>
    marvuno.com
  </div>

  <div class="street-address">
    <svg width="18" height="26" viewBox="0 0 18 26" aria-hidden="true">
      <path d="M9 0 C4 0 0 4 0 9 C0 15 9 26 9 26 C9 26 18 15 18 9 C18 4 14 0 9 0 Z" fill="var(--accent-red)"/>
      <circle cx="9" cy="9" r="3.5" fill="var(--paper)"/>
    </svg>
    <span>Street Name, City Name, State Zipcode</span>
  </div>
</section>

</body>
</html>
```